Super Greens Label for Supplement Bottle

We want to design a front label for a health supplement bottle. The product is called Meadow Twist Chews™. This will be a new product so there is no current website for the product. The focus is on supergreens that taste great and deliver support for energy, digestion, and immune defense.
We want it to be modern, vibrant and appealing.
Bottle size: standard size supplement CLEAR bottle size, with white child resistant cap and the label panel dimensions are 3” x 7”. The label should be primarily white and green, with a touch of red; (see color palettes)/it can also ONLY be white and green. See samples attached.
We are only focused on the front of the bottle design, not on the back, but leave space for the supplement panel and other text on the back.
So the text for the front of the bottle is:
RT Balden's
Meadow Twist Chews™
Super Greens Blend for:
Energy, Digestion, and Immune Support*
60 Gummies | Dietary Supplement
Raspberry Flavor Gummies
Off to side of the label:
Non-GMO
Vegan Friendly
Plant-Based
Gelatin Free
Colors
Designer to choose colors to be used in the design.

```html
<!DOCTYPE html>
<html lang="en">
<head>
<meta charset="utf-8">
<title>Meadow Twist Chews – Front Label</title>
<link rel="stylesheet" href="https://fonts.googleapis.com/css2?family=Oswald:wght@500&family=Poppins:wght@400;600&display=swap">
<style>
  :root {
    --white: #ffffff;
    --ink: #1e1e1e;
    --green-deep: #2f663a;
    --green-title: #2c6a38;
    --green-mid: #5a9449;
    --green-soft: #7fb06a;
    --red: #c8262c;
    --red-text: #b8262c;
    --red-art: #d9362f;
    --red-art-dark: #a8272a;
  }
  * { margin: 0; padding: 0; box-sizing: border-box; }
  html, body {
    width: 1195px; height: 1200px; overflow: hidden;
    background: var(--white);
  }
  .label {
    position: absolute; left: 381px; top: 96px;
    width: 433px; height: 1007px;
    border: 2px solid var(--ink);
    background: var(--white);
    overflow: hidden;
  }
  .bands { position: absolute; left: 0; top: 0; width: 433px; height: 1007px; z-index: 0; }
  .brand-tab {
    position: absolute; left: 142px; top: -2px;
    width: 157px; height: 157px;
    background: var(--green-mid);
    display: flex; align-items: flex-end; justify-content: center;
    padding-bottom: 26px;
    font-family: "Oswald", sans-serif; font-weight: 500;
    font-size: 35px; color: var(--white); letter-spacing: 0.2px;
  }
  .product-name {
    position: absolute; left: 0; top: 206px; width: 100%;
    text-align: center; font-family: "Poppins", sans-serif;
    line-height: 1;
  }
  .product-name .line-one {
    display: block; font-weight: 400; font-size: 54px; color: var(--green-title);
  }
  .product-name .line-two {
    display: block; font-weight: 600; font-size: 56px; color: var(--green-mid);
    margin-top: 4px;
  }
  .tagline {
    position: absolute; left: 0; top: 373px; width: 100%;
    text-align: center; font-family: "Poppins", sans-serif;
    font-size: 27px; line-height: 33px; color: var(--ink);
  }
  .fruit-art {
    position: absolute; left: 40px; top: 532px; z-index: 1;
    width: 185px; height: 160px; border-radius: 60px;
    background: radial-gradient(circle at 45% 45%, var(--red-art) 0%, var(--red-art) 55%, var(--red-art-dark) 100%);
  }
  .flavor {
    position: absolute; left: 232px; top: 562px; width: 170px; z-index: 2;
    text-align: center; font-family: "Oswald", sans-serif; font-weight: 500;
    font-size: 26px; line-height: 31px; color: var(--red-text);
  }
  .count-row {
    position: absolute; left: 100px; top: 763px; z-index: 2;
    display: flex; align-items: center; gap: 16px;
  }
  .count-badge {
    width: 84px; height: 84px; border-radius: 50%;
    background: var(--white); color: var(--green-deep);
    display: flex; align-items: center; justify-content: center;
    font-family: "Oswald", sans-serif; font-weight: 500; font-size: 46px;
  }
  .count-word {
    font-family: "Oswald", sans-serif; font-weight: 500;
    font-size: 38px; color: var(--white); margin-top: 18px;
  }
  .supplement {
    position: absolute; left: 0; top: 853px; width: 100%; z-index: 2;
    text-align: center; font-family: "Oswald", sans-serif; font-weight: 500;
    font-size: 27px; color: var(--white);
  }
</style>
</head>
<body>
  <main class="label">
    <svg class="bands" viewBox="0 0 433 1007" aria-hidden="true">
      <path d="M0 700 Q210 690 433 748 L433 758 Q210 718 0 730 Z" fill="var(--red)"/>
      <path d="M0 745 Q220 722 433 760 L433 940 L0 940 Z" fill="var(--green-mid)"/>
      <path d="M0 810 Q210 772 433 768 L433 940 L0 940 Z" fill="var(--green-deep)"/>
      <line x1="0" y1="875" x2="100" y2="875" stroke="var(--green-soft)" stroke-width="1.5"/>
      <line x1="330" y1="875" x2="433" y2="875" stroke="var(--green-soft)" stroke-width="1.5"/>
    </svg>

    <div class="brand-tab">Brand</div>

    <h1 class="product-name">
      <span class="line-one">Meadow Twist</span>
      <span class="line-two">Chews</span>
    </h1>

    <p class="tagline">Energy, Digestion, and<br>Immune Support</p>

    <div class="fruit-art" role="img" aria-label="Illustration of raspberries with green leaves"></div>

    <p class="flavor">Raspberry<br>Flavor Gummies</p>

    <div class="count-row">
      <div class="count-badge">60</div>
      <div class="count-word">Gummies</div>
    </div>

    <p class="supplement">Dietary Supplement</p>
  </main>
</body>
</html>
```